Need App for Impact Related Events

My app is to help with internal events. When you enter the prompted event code the next screen shows you everyone currently at the event. It will give you the ability to Start a conversation with someone you met at that event, or signal it is your turn to send a message. The next screen is a message thread with that person. I am looking for a design that incorporates the colors and ‘feel good’ emotion of our logo. I have pieced together a pretty good interpretation of what I’m looking for in the attached mockup by slicing and dicing designs. I also attached our logo mascot.Screens (see attached mockups)

Note 1: I do not like the picture on the screen used in screen one because it makes it seem like a dating app. I attached an alternative photo that can be used or present different ideas.

Note 2: On the login/signup screen (screen 2) I need an additional first and last name for login, you can try to fit this on one login screen or present a two step signup screen where that is presented in the second screen.

READ MOCKUP GUIDELINES UNDER Must Haves

Target Market(s)

People attending internal social impact events

Industry/Entity Type

Charity

Font styles to use
Sans Serif

Colors
86cfc6

Requirements
Must have
• Follow the screen mockups attached to project
• PLEASE READ
• I have provided a relatively close design of what I’m looking for in the mockups. Some screens need to be followed more closely to my design mockup than other. I have listed a guide below how how closely you should follow my mockup design exactly. Overall I would like to see some ideas of incorporating a few accent colors so it doesn’t appear SO Blue. I also attached some app inspiration designs I found from around the web
• Screen Mockup Guideline Follow %
• Screen 1: 65% - mostly on target, would like to see ways to make it not SO Blue and possibly creative places to add some explainer text describing the app
• Screen 2: 50% - general design idea is here, but more open
• Screen 3: 35% - a lot more room for design influence
• Screen 4: 70% - mostly on target, a little room for design influence/color scheme ideas
• Screen 5-6: 25% - a lot of room for design change/ideas/influence
• Screen 7-8: 80% - already very close to what I need, maybe open to slight sizing and color scheme ideas
• Screen 9: 15% - the most open for influence, only the general functionality of the screen is communicated here
Nice to have
• Please Read Mockup Guideline above. In large part I am looking for something to use some nice accent colors so it is not overwhelmingly blue and bring the whole design into a seamless style.
Should not have

```html
<!DOCTYPE html>
<html lang="en">
<head>
<meta charset="utf-8">
<title>Settings screens</title>
<link rel="stylesheet" href="https://fonts.googleapis.com/css2?family=Heebo:wght@300;400;500&family=Lato:wght@400&display=swap">
<style>
:root{
  --teal:#2fd6c6;
  --teal-deep:#23c7b8;
  --ink:#1c2a44;
  --ink-soft:#3a4660;
  --muted:#7e8796;
  --line:#e6e9ee;
  --sky:#3db3f6;
  --page:#ffffff;
  --screen:#f7f8fa;
  --card:#ffffff;
  --kb:#d2d6dc;
  --key:#ffffff;
  --key-dark:#adb3bc;
  --danger:#e8342f;
}
*{box-sizing:border-box;margin:0;padding:0}
html,body{width:1200px;height:1200px;overflow:hidden;background:var(--page)}
body{font-family:"Heebo",sans-serif;color:var(--ink);position:relative}
.screen{position:absolute;top:180px;width:390px;height:840px;border-radius:44px;background:var(--screen);overflow:hidden;border:1px solid var(--line)}
.screen--profile{left:141px}
.screen--rename{left:672px}
.status{position:absolute;top:0;left:0;right:0;height:50px;background:#fff}
.status__time{position:absolute;left:36px;top:18px;font-size:15px;font-weight:500}
.status__icons{position:absolute;right:24px;top:20px;display:flex;gap:6px}
.nav{position:absolute;top:50px;left:0;right:0;height:42px;background:#fff;border-bottom:1px solid var(--line);display:flex;align-items:center;justify-content:center}
.nav__back{position:absolute;left:18px;top:10px}
.nav__title{display:flex;align-items:center;gap:8px;font-size:19px;color:var(--ink-soft)}
.nav__mark{width:22px;height:22px;border-radius:50%;background:var(--teal)}
.card{position:absolute;left:16px;width:357px;background:var(--card);border-radius:8px;overflow:hidden}
.profile{top:113px;height:112px}
.profile__tab{position:absolute;left:0;top:0;width:52px;height:112px;background:var(--sky);border-radius:8px 0 0 8px}
.profile__avatar{position:absolute;left:15px;top:23px;width:72px;height:72px;border-radius:50%;background:linear-gradient(135deg,#c9b39a,#6d8d82);border:3px solid #fff}
.profile__cam{position:absolute;left:57px;top:68px;width:32px;height:32px;border-radius:50%;background:#fff;border:2px solid var(--teal);display:flex;align-items:center;justify-content:center}
.profile__name{position:absolute;left:108px;top:20px;font-size:22px;font-weight:400}
.profile__meta{position:absolute;left:110px;top:52px;font-size:14px;font-weight:300;line-height:23px}
.profile__edit{position:absolute;right:16px;top:24px;display:flex;gap:6px;align-items:center;font-size:14px}
.event-photo{position:absolute;left:0;right:0;background:linear-gradient(180deg,#5d7f86 0%,#7fa9a8 45%,#6fc8bc 78%,var(--teal) 100%)}
.event-tag{position:absolute;left:20px;display:flex;align-items:center;gap:10px;font-size:22px}
.event-tag__dot{width:48px;height:48px;border-radius:50%;background:#fff;border:4px solid #e9fbf8}
.code{top:242px;height:491px}
.code .event-photo{top:0;height:235px}
.code .event-tag{top:177px}
.code__label{position:absolute;left:21px;top:258px;font-size:18px;font-weight:400}
.code__value{position:absolute;left:21px;top:285px;font-size:27px;font-weight:500;color:var(--teal-deep);letter-spacing:.2px}
.code__actions{position:absolute;right:20px;top:262px;display:flex;gap:12px}
.code__cut{position:absolute;left:20px;right:20px;top:336px;border-top:2px dashed var(--line)}
.code__help{position:absolute;left:21px;top:356px;right:26px;font-size:20px;font-weight:300;line-height:25px;color:var(--ink-soft)}
.rename{top:114px;height:367px}
.rename .event-photo{top:0;height:235px}
.rename .event-tag{top:177px}
.rename__row{position:absolute;left:21px;right:21px;top:256px;display:flex;justify-content:space-between;font-size:18px}
.rename__action{color:var(--teal)}
.rename__field{position:absolute;left:21px;right:21px;top:296px;padding-bottom:12px;border-bottom:2px solid var(--teal);font-size:19px;font-weight:300;color:var(--muted)}
.keyboard{position:absolute;left:0;right:0;top:540px;bottom:0;background:var(--kb);padding:8px 3px 0;font-family:"Lato",sans-serif}
.kb-row{display:flex;justify-content:center;gap:5px;margin-bottom:12px}
.key{height:44px;width:34px;background:var(--key);border-radius:5px;box-shadow:0 1px 0 #8e949c;display:flex;align-items:center;justify-content:center;font-size:22px;color:#111}
.key--mod{background:var(--key-dark);width:44px}
.key--wide{font-size:16px;width:90px}
.key--space{width:93px;font-size:16px}
.key--return{width:90px;background:var(--key-dark);font-size:16px}
.kb-row--bottom .key{width:auto;padding:0 12px}
.kb-row--bottom .key--mod{width:90px}
.kb-extra{position:absolute;left:28px;right:40px;bottom:30px;display:flex;justify-content:space-between}
.home-bar{position:absolute;left:125px;bottom:8px;width:140px;height:5px;border-radius:3px;background:#111}
</style>
</head>
<body>

<section class="screen screen--profile">
  <div class="status">
    <span class="status__time">9:41</span>
    <div class="status__icons">
      <svg width="17" height="12" viewBox="0 0 17 12"><path d="M8.5 11l2-2.4a3 3 0 0 0-4 0zM3.5 5.8l1.6 1.6a5 5 0 0 1 6.8 0l1.6-1.6a7.4 7.4 0 0 0-10 0zM.5 2.8l1.6 1.6a9.3 9.3 0 0 1 12.8 0l1.6-1.6a11.6 11.6 0 0 0-16 0z" fill="#111"/></svg>
      <svg width="26" height="12" viewBox="0 0 26 12"><rect x=".5" y=".5" width="22" height="11" rx="3" fill="none" stroke="#111"/><rect x="2" y="2" width="19" height="8" rx="1.5" fill="#111"/><rect x="23.5" y="4" width="1.5" height="4" fill="#111"/></svg>
    </div>
  </div>
  <header class="nav">
    <svg class="nav__back" width="14" height="24" viewBox="0 0 14 24"><path d="M12 2L3 12l9 10" fill="none" stroke="#222" stroke-width="2.4" stroke-linecap="round"/></svg>
    <div class="nav__title"><span class="nav__mark"></span>Settings</div>
  </header>

  <article class="card profile">
    <div class="profile__tab"></div>
    <div class="profile__avatar" role="img" aria-label="Profile portrait of the user"></div>
    <div class="profile__cam">
      <svg width="16" height="13" viewBox="0 0 16 13"><path d="M1 3h3l1.5-2h5L12 3h3v9H1z" fill="none" stroke="var(--teal)" stroke-width="1.4"/><circle cx="8" cy="7.3" r="2.5" fill="none" stroke="var(--teal)" stroke-width="1.4"/></svg>
    </div>
    <h2 class="profile__name">Ravi Mehta</h2>
    <p class="profile__meta">+91 90000123xx<br>ravimehta@mailbox.com</p>
    <span class="profile__edit">Edit
      <svg width="18" height="18" viewBox="0 0 18 18"><path d="M3 13l9-9 2 2-9 9H3z" fill="none" stroke="#333" stroke-width="1.3"/><path d="M2 17h15" stroke="#333" stroke-width="1.3"/></svg>
    </span>
  </article>

  <article class="card code">
    <div class="event-photo" role="img" aria-label="Group of friends chatting over coffee in a café, teal tinted"></div>
    <div class="event-tag"><span class="event-tag__dot"></span>Hello Hive</div>
    <h3 class="code__label">Your Code</h3>
    <p class="code__value">AA4367CN6734</p>
    <div class="code__actions">
      <svg width="28" height="28" viewBox="0 0 28 28"><path d="M5 20L19 6l3 3L8 23H5z" fill="none" stroke="#333" stroke-width="1.6"/><path d="M3 27h24" stroke="#333" stroke-width="1.6"/></svg>
      <svg width="22" height="28" viewBox="0 0 22 28"><path d="M2 6h18M8 6V3h6v3M4 6l1.4 20h11.2L18 6M9 10v13M13 10v13" fill="none" stroke="var(--danger)" stroke-width="1.8"/></svg>
    </div>
    <div class="code__cut"></div>
    <p class="code__help">Give this code to the people at your location or event to allow them to connect to each other - kind of like a wifi password</p>
  </article>
  <div class="home-bar" style="display:none"></div>
</section>

<section class="screen screen--rename">
  <div class="status">
    <span class="status__time">9:41</span>
    <div class="status__icons">
      <svg width="17" height="12" viewBox="0 0 17 12"><path d="M8.5 11l2-2.4a3 3 0 0 0-4 0zM3.5 5.8l1.6 1.6a5 5 0 0 1 6.8 0l1.6-1.6a7.4 7.4 0 0 0-10 0zM.5 2.8l1.6 1.6a9.3 9.3 0 0 1 12.8 0l1.6-1.6a11.6 11.6 0 0 0-16 0z" fill="#111"/></svg>
      <svg width="26" height="12" viewBox="0 0 26 12"><rect x=".5" y=".5" width="22" height="11" rx="3" fill="none" stroke="#111"/><rect x="2" y="2" width="19" height="8" rx="1.5" fill="#111"/><rect x="23.5" y="4" width="1.5" height="4" fill="#111"/></svg>
    </div>
  </div>
  <header class="nav">
    <svg class="nav__back" width="14" height="24" viewBox="0 0 14 24"><path d="M12 2L3 12l9 10" fill="none" stroke="#222" stroke-width="2.4" stroke-linecap="round"/></svg>
    <div class="nav__title"><span class="nav__mark"></span>Settings</div>
  </header>

  <article class="card rename">
    <div class="event-photo" role="img" aria-label="Group of friends chatting over coffee in a café, teal tinted"></div>
    <div class="event-tag"><span class="event-tag__dot"></span>Hello Hive
      <svg width="22" height="22" viewBox="0 0 22 22"><path d="M4 15L15 4l3 3L7 18H4z" fill="none" stroke="var(--ink)" stroke-width="1.4"/><path d="M3 21h16" stroke="var(--ink)" stroke-width="1.4"/></svg>
    </div>
    <div class="rename__row"><span>Change Event Name</span><span class="rename__action">Change</span></div>
    <div class="rename__field">New Name</div>
  </article>

  <div class="keyboard">
    <div class="kb-row"><span class="key">q</span><span class="key">w</span><span class="key">e</span><span class="key">r</span><span class="key">t</span><span class="key">y</span><span class="key">u</span><span class="key">i</span><span class="key">o</span><span class="key">p</span></div>
    <div class="kb-row"><span class="key">a</span><span class="key">s</span><span class="key">d</span><span class="key">f</span><span class="key">g</span><span class="key">h</span><span class="key">j</span><span class="key">k</span><span class="key">l</span></div>
    <div class="kb-row">
      <span class="key key--mod"><svg width="20" height="18" viewBox="0 0 20 18"><path d="M10 2L2 10h4v6h8v-6h4z" fill="none" stroke="#222" stroke-width="1.5"/></svg></span>
      <span class="key">z</span><span class="key">x</span><span class="key">c</span><span class="key">v</span><span class="key">b</span><span class="key">n</span><span class="key">m</span>
      <span class="key key--mod"><svg width="24" height="16" viewBox="0 0 24 16"><path d="M7 1h16v14H7L1 8z" fill="none" stroke="#222" stroke-width="1.5"/><path d="M11 5l6 6M17 5l-6 6" stroke="#222" stroke-width="1.5"/></svg></span>
    </div>
    <div class="kb-row kb-row--bottom">
      <span class="key key--mod key--wide">123</span>
      <span class="key key--space">space</span>
      <span class="key">@</span>
      <span class="key">.</span>
      <span class="key key--return">return</span>
    </div>
    <div class="kb-extra">
      <svg width="28" height="28" viewBox="0 0 28 28"><circle cx="14" cy="14" r="12" fill="none" stroke="#555" stroke-width="1.6"/><circle cx="10" cy="11" r="1.5" fill="#555"/><circle cx="18" cy="11" r="1.5" fill="#555"/><path d="M8 16a6 6 0 0 0 12 0z" fill="none" stroke="#555" stroke-width="1.5"/></svg>
      <svg width="16" height="28" viewBox="0 0 16 28"><rect x="4" y="1" width="8" height="16" rx="4" fill="none" stroke="#555" stroke-width="1.6"/><path d="M1 13a7 7 0 0 0 14 0M8 20v6M4 26h8" fill="none" stroke="#555" stroke-width="1.6"/></svg>
    </div>
    <div class="home-bar"></div>
  </div>
</section>

</body>
</html>
```